Payday Lending App Interface Design

Hello, we are building a payday lending application, Lendora, that lend people money. I have drafted some of the screens that show the functionalities we have at the moment, please find the screens in attachments.
The elements in the screens are placed just to show what should be included in those screens, it's not necessary to follow the same layout. If you have better design ideas, you are very welcomed to show off your talent.
I think what we want is a style guide so that we can apply the same style to any screens that are similar to the ones I attached. We really like
the style as in the attached image called Style.png. We might want something similar - a simple, clean design yet fun and engaging. Customised graphical elements such as icons, illustrations are preferable.
Apart from the attached screens, we might also need a design for the On Board screen and the Login/Sign Up screen too.
Our logo colour is in yellow and black. Perhaps we will have a similar colour theme. I also attached the logo file, icon-Lendora.png, if you would like to put it in your design.
Please message me if you need further information.
Regards
Target Market(s)
Young people that doesn't have strong income
Look and feel

```html
<!DOCTYPE html>
<html lang="en">
<head>
<meta charset="UTF-8">
<title>Lendora – Welcome</title>
<link rel="stylesheet" href="https://fonts.googleapis.com/css2?family=Mulish:wght@300;800&family=Roboto:wght@500&display=swap">
<style>
  :root {
    --brand-yellow: #FAD40C;
    --ink: #121212;
    --ink-soft: #2a2a22;
    --cta-orange: #D9651E;
    --cta-text: #ffffff;
    --credit-grey: #8f8a6a;
    --figure-top: #f1b04a;
    --figure-mid: #e9a24a;
    --figure-low: #5f8fae;
    --page-bg: #ffffff;
  }
  * { margin: 0; padding: 0; box-sizing: border-box; }
  html, body {
    width: 1200px;
    height: 2597px;
    overflow: hidden;
    background: var(--page-bg);
  }
  .welcome-screen {
    position: relative;
    width: 1200px;
    height: 2597px;
    background: var(--brand-yellow);
    border-radius: 110px;
    overflow: hidden;
    font-family: "Mulish", sans-serif;
    color: var(--ink);
  }
  .brand-name {
    position: absolute;
    left: 96px;
    top: 92px;
    font-family: "Mulish", sans-serif;
    font-weight: 800;
    font-size: 64px;
    line-height: 1;
    color: var(--ink);
  }
  .welcome-title {
    position: absolute;
    left: 212px;
    top: 680px;
    font-weight: 800;
    font-size: 104px;
    line-height: 145px;
    letter-spacing: -0.5px;
  }
  .welcome-tagline {
    position: absolute;
    left: 212px;
    top: 990px;
    width: 620px;
    font-weight: 300;
    font-size: 49px;
    line-height: 87px;
    color: var(--ink-soft);
  }
  .cta-button {
    position: absolute;
    left: 212px;
    top: 1322px;
    width: 386px;
    height: 101px;
    border: none;
    border-radius: 36px;
    background: var(--cta-orange);
    color: var(--cta-text);
    font-family: "Roboto", sans-serif;
    font-weight: 500;
    font-size: 41px;
    display: flex;
    align-items: center;
    justify-content: center;
  }
  .hero-figure {
    position: absolute;
    left: 783px;
    top: 435px;
    width: 417px;
    height: 1913px;
    border-radius: 200px 0 0 60px;
    background: linear-gradient(180deg, var(--figure-top) 0%, var(--figure-mid) 30%, var(--figure-low) 45%, var(--figure-low) 100%);
    opacity: 0.85;
  }
  .illustration-credit {
    position: absolute;
    left: 0;
    right: 0;
    top: 2494px;
    text-align: center;
    font-family: "Roboto", sans-serif;
    font-weight: 500;
    font-size: 26px;
    color: var(--credit-grey);
    opacity: 0.8;
  }
</style>
</head>
<body>
  <main class="welcome-screen">
    <div class="brand-name">Lendora</div>

    <h1 class="welcome-title">Welcome<br>to Lendora!</h1>
    <p class="welcome-tagline">The simplest way to lend you money right away....</p>

    <button class="cta-button" type="button">Get Started</button>

    <div class="hero-figure" role="img" aria-label="3D illustration of a young woman with orange hair, yellow top and blue jeans holding a tablet"></div>

    <p class="illustration-credit">3D Illustration by Pixmoor</p>
  </main>
</body>
</html>
```